International house cleaning business needs Marketing Landing Page for improving user acquisition

We are in need of an additional marketing Landing Page that we can use to test and improve our user acquisition. We will be looking at a minimum of one page selection, but are open to awarding up to 5 depending on the quality of work and the different variables to test.

Our current homepages are www.tidlyo.com and https://www.tidlyo.com/lps/firstnhours.aspx?c=MARKETING39&city=Toronto&gclid=CIqXg7z_wsECFUKCMgodknwAGA and we are looking for ways that will improve 1) Account Creation and 2) Appointment Bookings by making them more simple. Please look at the entire process and address the main issues in the Landing Page that you create.

Competitors include www.scrubvix.com and www.pravelo.com

The design will be entirely up to your discretion, however the required aspects are below:

1) Maintain Corporate color scheme
2) Target audience are new users coming from offer based marketing campaigns
3) Will need an area of the page with a changeable 'offer message'
4) The offer area mentioned above should also be easily removable if there is no offer
5) The focus is on new users but we will still need to have a visible 'sign in button' for returning users
6) Linkumo login and create account with email CTA's both must be large and visible
7) Opt-in for eNewsletter button when email address is collected
8) We also have a short informative video so feel free to incorporate that in a version

General Ideas:

*email collection on Landing Page to start engagement early
*email and postal code collection on Landing Page to start engagement early
*general information and booking form on the HP to reduce the click needed to get to account creation or booking
*"Tell Us About Your Place" info (# of beds and # of baths) on HP to get process started (similar to www.nestqor.com)

Good Examples:

www.linkumo.com (merges info and sign-up)
www.nestqor.com (early engagement)
www.raxo.com (early engagement)

```html
<!DOCTYPE html>
<html lang="en">
<head>
<meta charset="utf-8">
<title>Tidlyo.com – 3 Hour Home Cleaning</title>
<link rel="stylesheet" href="https://fonts.googleapis.com/css2?family=Montserrat:wght@500;600&family=Open+Sans:ital,wght@0,400;0,600;0,700;1,400&display=swap">
<style>
:root{
  --teal:#176f83;
  --teal-deep:#1b6d7e;
  --coral:#ec6a5e;
  --green:#45c4a6;
  --green-dark:#2f9f86;
  --blue:#40559a;
  --blue-dark:#2f4079;
  --page:#fbfbf9;
  --band:#efefed;
  --panel:#f7f4ec;
  --ink:#444;
  --muted:#8a8a8a;
}
*{box-sizing:border-box;margin:0;padding:0}
html,body{width:1200px;height:1198px;overflow:hidden}
body{position:relative;background:var(--page);font-family:"Open Sans",Arial,sans-serif;color:var(--ink)}
.site-header{position:absolute;left:0;top:0;width:1200px;height:98px;background:linear-gradient(#f4f3ee,#e7e5dd);border-bottom:1px solid #e0ded6}
.brand{position:absolute;left:128px;top:24px;font-family:"Open Sans",Arial,sans-serif;font-weight:700;font-size:40px;color:var(--coral);letter-spacing:-.5px}
.main-nav{position:absolute;right:132px;top:37px;display:flex;gap:36px}
.main-nav a{font-size:14px;color:#555;text-decoration:none;letter-spacing:.2px}
.offer-title{position:absolute;left:128px;top:132px;font-family:"Montserrat",Arial,sans-serif;font-weight:600;font-size:43px;color:var(--teal);letter-spacing:.3px;white-space:nowrap}
.offer-title em{font-style:normal;color:var(--coral)}
.signup-panel{position:absolute;left:128px;top:224px;width:401px;height:372px;background:var(--panel)}
.signup-panel h2{position:absolute;left:12px;top:32px;font-weight:400;font-size:20px;line-height:31px;color:var(--teal-deep)}
.signup-panel h2 strong{color:var(--green);font-weight:700;font-size:22px}
.signup-panel p{position:absolute;left:12px;top:112px;width:380px;font-size:14px;line-height:19px;color:#555}
.signup-panel p b{font-weight:600;color:#333}
.field{position:absolute;background:#fff;border:1px solid #d9d6cd;border-radius:2px;font-size:13.5px;font-style:italic;color:#999;padding-left:9px;display:flex;align-items:center}
.field-email{left:30px;top:176px;width:302px;height:37px}
.field-select{top:233px;width:147px;height:36px}
.field-select::after{content:"";position:absolute;right:0;top:0;width:22px;height:100%;border-left:1px solid #d9d6cd;background:linear-gradient(#999,#999) no-repeat}
.field-select .caret{position:absolute;right:7px;top:15px;border:4px solid transparent;border-top:5px solid #888}
.field-select.beds{left:30px}
.field-select.baths{left:184px}
.field-select::after{background:none}
.btn-proceed{position:absolute;left:31px;top:292px;width:300px;height:45px;background:var(--green);border-bottom:4px solid var(--green-dark);border-radius:2px;color:#fff;font-weight:700;font-size:20px;letter-spacing:.5px;display:flex;align-items:center;justify-content:center;gap:12px}
.video{position:absolute;left:529px;top:224px;width:539px;height:372px;background:linear-gradient(100deg,#4d3f68 0%,#5a4a6e 25%,#6b5a4e 50%,#3e4548 78%,#3b4246 100%)}
.video svg{position:absolute;left:195px;top:111px}
.cta-row{position:absolute;top:628px;left:0;width:1200px;height:58px}
.btn{position:absolute;top:0;height:58px;border-radius:2px;color:#fff;display:flex;align-items:center;justify-content:center;font-size:20px}
.btn-quote{left:330px;width:218px;background:linear-gradient(#ef7a6e,#e8605a);border-bottom:4px solid #c94c45;font-size:21px}
.btn-social{left:648px;width:218px;background:linear-gradient(#4b61a8,#3d5194);border-bottom:4px solid var(--blue-dark);font-size:19px}
.or{position:absolute;left:580px;top:12px;font-size:20px;color:#333}
.benefits{position:absolute;left:0;top:748px;width:1200px;height:370px;background:var(--band)}
.promo{position:absolute;left:129px;top:46px;width:460px;height:264px;background:#d8d8d6;border-bottom:4px solid #c8c8c6}
.promo-photo{position:absolute;left:8px;top:8px;width:444px;height:246px;background:linear-gradient(90deg,#e6e6e4 0%,#f3f3f1 45%,#dfe6e3 70%,#c9dcd7 100%)}
.badge{position:absolute;left:38px;top:19px;width:142px;height:142px;border-radius:50%;background:var(--teal);border:2px dashed rgba(255,255,255,.25);color:#fff;text-align:center}
.badge .price{display:block;margin-top:18px;font-weight:700;font-size:30px}
.badge .line{display:block;font-size:17px;line-height:27px}
.badge .line b{font-weight:700}
.benefits h3{position:absolute;left:610px;top:50px;font-weight:400;font-size:28px;line-height:30px;color:var(--teal)}
.checklist{position:absolute;left:638px;top:134px;list-style:none}
.checklist li{font-size:18px;line-height:29px;color:#444;display:flex;align-items:center;gap:7px}
.learn-more{position:absolute;left:637px;top:275px;font-size:13.5px;color:var(--teal);text-decoration:underline}
.site-footer{position:absolute;left:0;top:1118px;width:1200px;height:80px}
.footer-links{position:absolute;left:129px;top:22px;display:flex;gap:22px}
.footer-links a{font-size:12.5px;color:#555;text-decoration:none}
.copyright{position:absolute;left:129px;top:46px;font-size:10px;color:#666}
.social{position:absolute;left:905px;top:28px;display:flex;gap:18px}
.social span{display:block;width:27px;height:27px;border-radius:2px}
.social .s1{background:#3b5a9a}.social .s2{background:#33a9dd}.social .s3{background:#333}.social .s4{background:#c8302a}
</style>
</head>
<body>
<header class="site-header">
  <div class="brand">Tidlyo.com</div>
  <nav class="main-nav">
    <a href="#">HELP</a>
    <a href="#">ABOUT US</a>
    <a href="#">STANDARD CLEANING CHECKLIST</a>
  </nav>
</header>

<h1 class="offer-title">GET A <em>3 HOUR</em> HOME CLEANING ONLY <em>$39</em>!</h1>

<section class="signup-panel">
  <h2>Do you really have the time to clean<br><strong>YOUR HOME?</strong></h2>
  <p>Give your home a fresh, thorough cleaning by Tidlyo professionals. Just schedule when and <b>we'll do the rest</b>!</p>
  <div class="field field-email">Enter your Email Address</div>
  <div class="field field-select beds">No. of bedrooms<i class="caret"></i></div>
  <div class="field field-select baths">No. of bathrooms<i class="caret"></i></div>
  <div class="btn-proceed">PROCEED
    <svg width="22" height="22" viewBox="0 0 22 22"><circle cx="11" cy="11" r="10" fill="#fff"/><path d="M6 11h8M10.5 6.5L15 11l-4.5 4.5" stroke="#45c4a6" stroke-width="2.6" fill="none" stroke-linecap="round" stroke-linejoin="round"/></svg>
  </div>
</section>

<div class="video" role="img" aria-label="Video still of a cleaner vacuuming an office floor">
  <svg width="150" height="150" viewBox="0 0 150 150"><circle cx="75" cy="75" r="71" fill="rgba(0,0,0,.15)" stroke="#fff" stroke-width="7"/><path d="M56 42L109 75L56 108Z" fill="#fff"/></svg>
</div>

<div class="cta-row">
  <div class="btn btn-quote">Get a Quote Now</div>
  <span class="or">-or-</span>
  <div class="btn btn-social">Book with Linkumo</div>
</div>

<section class="benefits">
  <div class="promo">
    <div class="promo-photo" role="img" aria-label="Smiling cleaner holding a mop and bucket in a bright room"></div>
    <div class="badge"><span class="price">$39</span><span class="line">Cleaning for</span><span class="line"><b>3 Hours</b></span></div>
  </div>
  <h3>Lorem ipsum is a dummy text only<br>dolor sit amet cons ectetur.</h3>
  <ul class="checklist">
    <li><svg width="15" height="13" viewBox="0 0 15 13"><rect width="13" height="12" y="1" fill="#d8efe9"/><path d="M2 7l3.5 3.5L14 1" stroke="#3fbf9f" stroke-width="2.4" fill="none"/></svg>Fully screened cleaners</li>
    <li><svg width="15" height="13" viewBox="0 0 15 13"><rect width="13" height="12" y="1" fill="#d8efe9"/><path d="M2 7l3.5 3.5L14 1" stroke="#3fbf9f" stroke-width="2.4" fill="none"/></svg>60-point checklist</li>
    <li><svg width="15" height="13" viewBox="0 0 15 13"><rect width="13" height="12" y="1" fill="#d8efe9"/><path d="M2 7l3.5 3.5L14 1" stroke="#3fbf9f" stroke-width="2.4" fill="none"/></svg>Friendly client services</li>
    <li><svg width="15" height="13" viewBox="0 0 15 13"><rect width="13" height="12" y="1" fill="#d8efe9"/><path d="M2 7l3.5 3.5L14 1" stroke="#3fbf9f" stroke-width="2.4" fill="none"/></svg>Satisfaction assured</li>
  </ul>
  <a class="learn-more" href="#">Learn More</a>
</section>

<footer class="site-footer">
  <nav class="footer-links">
    <a href="#">Standard Cleaning Checklist</a>
    <a href="#">About Us</a>
    <a href="#">Terms Of Use</a>
    <a href="#">Privacy Policy</a>
  </nav>
  <p class="copyright">Copyright©tidlyo.com 2014. All Rights Reserved</p>
  <div class="social" aria-label="Social links">
    <span class="s1"></span><span class="s2"></span><span class="s3"></span><span class="s4"></span>
  </div>
</footer>
</body>
</html>
```